Companybrochure for Consulting & Financing Firm

I need to have a Company Brochure asap for our company. We have a website that describes what we do, but we need also a brochure, that can be sent by PDF of eventually be printed as well.

The brochure should be short but nice and appealing to the customers.

We provide professional management consulting and help our customers to get finance for very diferent projects. Our business has a lot to do with personal relations, but also we are very professional in the way we work and how develop the solutions for our clients. Our clients are mainly government-owned firm, but also private trading companies and wealthy private investors.

Our customers are mainly in Latin America, but the company is headquater is in Switzerland. We are opening offices in Panama and Caracas, this should be easaly be adabtable later.

Please have a look at our website www.brevalto.ch. In the brochure, we would segment our services in 1.) Project Developments 2.) Management Conulting 3.) Investment Management and 4.) Finance Solutions.

Also do have a look at www.brevalto.ch
(Click E for the English version)

I managed to put the Mock-Up to the Website.
It is actually not really a mock-up, it is a version I have designed myself.
Well as I am not a designer, I hope you can make it much better.
The content however is what I would put in any other design as well.

Target Market(s)

Top Management, Investors, Entrepreneurs, Government Officials

Industry/Entity Type

Management Consulting

Requirements
Must have
• Design should reflect this image elements:

We are entrepreneurs.
We are comitted to get things done.
We work closely with the client side by side.
We are a professional partner.
We are not afraid of delivering unconventional solutions.
We look at the problem from various angles.
We analyse, develop solutions and implent results.
Should not have
• Typical US-American style elements. We do not want to give the impression of being a US company.

We do not want to appear to be neo-liberal. We are a politically neutral professional consulting firm.

```html
<!DOCTYPE html>
<html lang="en">
<head>
<meta charset="utf-8">
<title>Brevalto AG – Project Development</title>
<link rel="stylesheet" href="https://fonts.googleapis.com/css2?family=Roboto:wght@300;400;500;700&family=Arimo:wght@400;700&display=swap">
<style>
  :root {
    --ink: #1f1f1f;
    --logo-grey: #3a3a3a;
    --bar-black: #1a1a1a;
    --orange: #e46c0e;
    --orange-text: #e8711b;
    --red: #b51b0c;
    --paper: #ffffff;
  }
  * { margin: 0; padding: 0; box-sizing: border-box; }
  html, body { width: 1200px; height: 862px; overflow: hidden; background: var(--paper); }
  .page { position: relative; width: 1200px; height: 862px; font-family: "Roboto", Arial, sans-serif; color: var(--ink); }

  .top-rule { position: absolute; left: 35px; top: 79px; width: 1133px; height: 9px; background: var(--bar-black); }

  .brand { position: absolute; right: 62px; top: 136px; font-weight: 500; font-size: 40px; letter-spacing: -0.3px; color: var(--logo-grey); line-height: 1; }

  .hero { position: absolute; left: 35px; top: 206px; width: 1133px; height: 254px; overflow: hidden; }
  .hero svg { display: block; }
  .hero-title { position: absolute; left: 30px; top: 112px; color: #fff; font-family: "Arimo", Arial, sans-serif; line-height: 0.84; }
  .hero-title .line-light { display: block; font-weight: 400; font-size: 72px; letter-spacing: -5px; margin-left: 12px; }
  .hero-title .line-bold { display: block; font-weight: 700; font-size: 74px; letter-spacing: -5.5px; }

  .intro { position: absolute; left: 65px; top: 490px; width: 650px; }
  .intro .lead { color: var(--orange-text); font-weight: 700; font-size: 19.5px; line-height: 27px; margin-bottom: 37px; }
  .intro .body { font-weight: 700; font-size: 16.5px; line-height: 23px; text-align: justify; margin-bottom: 21px; color: var(--ink); }

  .line { display: block; text-align: justify; text-align-last: justify; }
  .line.last { text-align-last: left; }

  .testimonials { position: absolute; left: 727px; top: 489px; width: 411px; }
  .testimonials-head { position: relative; height: 43px; background: var(--bar-black); color: #fff; font-weight: 700; font-size: 17px; display: flex; align-items: center; justify-content: center; letter-spacing: 0.2px; }
  .testimonials-head::before { content: ""; position: absolute; left: 0; top: 0; border-top: 22px solid var(--orange); border-right: 22px solid transparent; }
  .testimonials-body { background: var(--orange); color: #fff; font-weight: 300; font-size: 14px; line-height: 21.6px; padding: 20px 13px 10px; height: 251px; overflow: hidden; }
</style>
</head>
<body>
<div class="page">
  <div class="top-rule"></div>
  <div class="brand">Brevalto AG</div>

  <section class="hero">
    <svg width="1133" height="254" viewBox="0 0 1133 254" role="img" aria-label="Photograph of a radio telescope dish array in a desert landscape, overlaid with diagonal orange and red bands">
      <defs>
        <linearGradient id="sky" x1="0" y1="0" x2="0" y2="1">
          <stop offset="0" stop-color="#9a9a9a"/>
          <stop offset="0.6" stop-color="#6e6e6e"/>
          <stop offset="1" stop-color="#1e1e1e"/>
        </linearGradient>
      </defs>
      <rect width="1133" height="254" fill="url(#sky)"/>
      <polygon points="150,0 382,0 132,254 -100,254" fill="#d0530f" opacity="0.9"/>
      <polygon points="382,0 640,0 390,254 132,254" fill="#b51b0c" opacity="0.88"/>
      <polygon points="640,0 735,0 485,254 390,254" fill="#e0761a" opacity="0.85"/>
      <polygon points="950,0 1133,0 1133,60 945,254 700,254" fill="#d65a12" opacity="0.85"/>
    </svg>
    <h1 class="hero-title"><span class="line-light">PROJECT</span><span class="line-bold">DEVELOPMENT</span></h1>
  </section>

  <section class="intro">
    <p class="lead">Sometimes a project with high potential has to be<br>developed before its economic value becomes apparent.</p>
    <p class="body"><span class="line">In such situations, we participate financially in the project and commit</span><span class="line last">ourselves as entrepreneurs together with the owners.</span></p>
    <p class="body">We also take care of project management.</p>
  </section>

  <aside class="testimonials">
    <h2 class="testimonials-head">WHAT OUR CLIENTS HAVE TO SAY...</h2>
    <p class="testimonials-body">
      <span class="line">Lorem Ipsum is simply dummy text of the printing and</span>
      <span class="line">typesetting industry. Lorem Ipsum has been the</span>
      <span class="line">industry's standard dummy text ever since the 1500s,</span>
      <span class="line">when an unknown printer took a galley of type and</span>
      <span class="line">scrambled it to make a type specimen book. It has</span>
      <span class="line">survived not only five centuries, but also the leap into</span>
      <span class="line">electronic typesetting, remaining essentially unchanged.</span>
      <span class="line">It was popularised in the 1960s with the release of</span>
      <span class="line">Typeline sheets containing Lorem Ipsum passages, and</span>
      <span class="line last">more recently with desktop publishing software like</span>
    </p>
  </aside>
</div>
</body>
</html>
```